Gutschein-Design für Lorenzo Restaurant
Zielgruppe
Pizzeria Restaurant à la carte/ Das Design soll Jedem gefallen, mir, Familien, Pärchen, etc.
Aufgabenstellung
Die Gutscheine werden von unserem Kassensystem bedruckt. Die Größe ist ca. 95 mm/ 80 mm. Dieser Bon sollte in die Gutschein-Hülle, die ich jetzt brauche eingesteckt sein. Die Masse sollen 105x105 mm sein, offen 105x210 mm .
Text:
Auf Seite 1:
- Das Logo
- Geschenk-Gutschein
Auf Seite 2:
- Der Gutschein kann für Vieles gut sein
- In unserem Fall lässt unsere reichhaltige Karte viele Möglichkeiten offen
- Auf jeden Fall wird bestimmt geschlemmt, geschmaust und genossen
- Wir wünschen guten Appetit
Auf Seite 3 für die Druckerei:
- 2 Halbkreise gestanzt und 1x gerillt, rundum auf Endformat beschnitten.
- 1-Bruch Falz
Hier gehört der Gutschein-Bon 95/80 mm eingesteckt
Auf Seite 4:
Lorenzo
Restaurantbetriebsgesellschaft m.b.H.
www.lorenzo-trattoria.at
Im Dateiupload habe ich als ein Beispiel die jetzigen Gutscheinhuelle beigefügt.
MfG

```html
<!DOCTYPE html>
<html lang="de">
<head>
<meta charset="utf-8">
<title>Lorenzo – Gutschein-Hülle</title>
<link rel="stylesheet" href="https://fonts.googleapis.com/css2?family=Lobster&display=swap">
<style>
  :root {
    --wine: #5a0002;
    --straw: #ecdf85;
    --cream: #ffffff;
    --die-line: #f01ef0;
  }
  html, body {
    margin: 0;
    padding: 0;
    width: 1200px;
    height: 600px;
    overflow: hidden;
    background: var(--straw);
  }
  .sleeve {
    position: relative;
    width: 1200px;
    height: 600px;
    display: flex;
  }
  .panel-message {
    width: 600px;
    height: 600px;
    background: var(--wine);
    color: var(--cream);
    font-family: "Lobster", cursive;
    position: relative;
  }
  .message-line {
    position: absolute;
    left: 0;
    width: 604px;
    margin: 0;
    text-align: center;
    font-size: 30px;
    font-weight: 400;
    line-height: 1;
  }
  .line-1 { top: 88px; }
  .line-2 { top: 151px; }
  .line-3 { top: 214px; }
  .line-4 { top: 277px; }
  .line-5 { top: 340px; }
  .line-closing { top: 466px; }
  .panel-front {
    position: relative;
    width: 600px;
    height: 600px;
    background: var(--straw);
  }
  .die-cuts {
    position: absolute;
    inset: 0;
  }
  .brand {
    position: absolute;
    left: 150px;
    top: 245px;
    width: 300px;
    display: flex;
    align-items: center;
    justify-content: center;
    gap: 18px;
    color: var(--wine);
    font-family: "Lobster", cursive;
    font-size: 72px;
    line-height: 1;
  }
  .brand-dot {
    width: 26px;
    height: 26px;
    border-radius: 50%;
    background: var(--wine);
  }
</style>
</head>
<body>
  <main class="sleeve">
    <section class="panel-message">
      <p class="message-line line-1">Ein Gutschein kann für Vieles gut sein.</p>
      <p class="message-line line-2">In unserem Fall lässt unsere</p>
      <p class="message-line line-3">reichhaltige Karte viele Möglichkeiten offen.</p>
      <p class="message-line line-4">Auf jeden Fall wird bestimmt geschlemmt,</p>
      <p class="message-line line-5">geschmaust und genossen.</p>
      <p class="message-line line-closing">Wir wünschen guten Appetit.</p>
    </section>
    <section class="panel-front">
      <svg class="die-cuts" width="600" height="600" viewBox="0 0 600 600" aria-hidden="true">
        <path d="M204 65 A89 89 0 0 0 382 65" fill="none" stroke="var(--die-line)" stroke-width="1.6" stroke-dasharray="10 6 3 6"/>
        <path d="M202 535 A89 89 0 0 1 380 535" fill="none" stroke="var(--die-line)" stroke-width="1.6" stroke-dasharray="10 6 3 6"/>
      </svg>
      <div class="brand">
        <span class="brand-name">Lorenzo</span>
        <span class="brand-dot"></span>
      </div>
    </section>
  </main>
</body>
</html>
```